Business Cards/Stationary for CIO Outsourcing Company
Velmora Solutions
Use same font as used in my logo
Dorian Halbrook
Partner
Four Maple Ridge Plaza
Suite 240
Harlow Springs, Texas 75990
dhalbrook@govelmora.com
www.govelmora.com
Logo icon can be shown separate from the name if necessary on stationary.

```html
<!DOCTYPE html>
<html lang="en">
<head>
<meta charset="utf-8">
<title>Velmora Solutions – Business Card</title>
<link href="https://fonts.googleapis.com/css2?family=Cinzel:wght@400;600&family=Cormorant+Garamond:wght@500;600&display=swap" rel="stylesheet">
<style>
  :root {
    --backdrop: #e9e6e2;
    --brand-red: #b3272c;
    --brand-red-dark: #9c2126;
    --card-white: #ffffff;
    --ink: #3b3b3b;
    --ink-soft: #6a6a6a;
  }
  * { margin: 0; padding: 0; box-sizing: border-box; }
  html, body { width: 1200px; height: 629px; overflow: hidden; }
  body {
    background: var(--backdrop);
    font-family: "Cormorant Garamond", Georgia, serif;
    color: var(--ink);
    position: relative;
  }
  .card {
    position: absolute;
    top: 165px;
    width: 520px;
    height: 297px;
    box-shadow: 0 6px 18px rgba(0,0,0,0.18);
  }
  /* Back of card */
  .card-back {
    left: 60px;
    background: var(--brand-red);
    color: var(--card-white);
  }
  .card-back .brand {
    position: absolute;
    top: 112px;
    left: 0; right: 0;
    display: flex;
    align-items: center;
    justify-content: center;
    gap: 12px;
  }
  .card-back .brand-dot {
    width: 18px; height: 18px;
    border-radius: 50%;
    background: var(--card-white);
  }
  .card-back .brand-name {
    font-family: "Cinzel", serif;
    font-weight: 600;
    font-size: 34px;
    letter-spacing: 3px;
  }
  .card-back .website {
    position: absolute;
    bottom: 40px;
    left: 0; right: 0;
    text-align: center;
    font-family: "Cinzel", serif;
    font-size: 12px;
    letter-spacing: 3px;
  }
  /* Front of card */
  .card-front {
    left: 620px;
    background: var(--card-white);
  }
  .card-front .brand {
    position: absolute;
    top: 46px;
    left: 150px;
    display: flex;
    align-items: center;
    gap: 12px;
  }
  .card-front .brand-square {
    width: 20px; height: 20px;
    background: var(--brand-red);
  }
  .card-front .brand-name {
    font-family: "Cinzel", serif;
    font-weight: 600;
    font-size: 40px;
    letter-spacing: 3px;
    color: var(--brand-red);
  }
  .person {
    position: absolute;
    top: 128px;
    left: 40px;
    font-size: 12px;
    line-height: 1.35;
  }
  .person .name {
    font-family: "Cinzel", serif;
    font-size: 12px;
    color: var(--brand-red);
    letter-spacing: 1px;
  }
  .person .title { color: var(--ink-soft); margin-bottom: 14px; font-size: 12px; letter-spacing: 1px; }
  .person .address { font-family: "Cinzel", serif; font-size: 10px; letter-spacing: 1px; color: var(--ink); }
  .contact {
    position: absolute;
    top: 120px;
    left: 282px;
    list-style: none;
    font-size: 12px;
    line-height: 1;
  }
  .contact li { display: flex; align-items: center; gap: 8px; margin-bottom: 6px; }
  .contact svg { width: 12px; height: 12px; flex: none; }
  .card-front .band {
    position: absolute;
    left: 0; right: 0; bottom: 0;
    height: 44px;
    background: var(--brand-red);
    color: var(--card-white);
    display: flex;
    align-items: center;
    justify-content: flex-end;
    padding-right: 36px;
    font-family: "Cinzel", serif;
    font-size: 12px;
    letter-spacing: 3px;
  }
  .card-front .band::before {
    content: "";
    position: absolute;
    left: 0; right: 0; top: -5px;
    height: 2px;
    background: var(--brand-red-dark);
  }
</style>
</head>
<body>
  <section class="card card-back" aria-label="Card back">
    <div class="brand">
      <span class="brand-dot"></span>
      <span class="brand-name">VELMORA</span>
    </div>
    <p class="website">www.govelmora.com</p>
  </section>

  <section class="card card-front" aria-label="Card front">
    <div class="brand">
      <span class="brand-square"></span>
      <span class="brand-name">VELMORA</span>
    </div>

    <div class="person">
      <p class="name">Dorian Halbrook</p>
      <p class="title">Partner</p>
      <p class="address">Four Maple Ridge Plaza<br>Suite 240<br>Harlow Springs, Texas 75990</p>
    </div>

    <ul class="contact">
      <li>
        <svg viewBox="0 0 12 12"><circle cx="6" cy="6" r="6" fill="#b3272c"/><path d="M4 3.2l1 1.4-.6.7a4 4 0 0 0 2.3 2.3l.7-.6 1.4 1-.6 1A5 5 0 0 1 3 4z" fill="#fff"/></svg>
        (555) 010-4821
      </li>
      <li>
        <svg viewBox="0 0 12 12"><circle cx="6" cy="6" r="6" fill="#b3272c"/><rect x="3.3" y="4" width="5.4" height="4" fill="#fff"/></svg>
        (555) 010-4867
      </li>
      <li>
        <svg viewBox="0 0 12 12"><circle cx="6" cy="6" r="6" fill="#b3272c"/><path d="M3 4h6v4H3z M3 4l3 2 3-2" fill="none" stroke="#fff" stroke-width=".9"/></svg>
        dhalbrook@govelmora.com
      </li>
      <li>
        <svg viewBox="0 0 12 12"><circle cx="6" cy="6" r="6" fill="#b3272c"/><circle cx="6" cy="6" r="2.8" fill="none" stroke="#fff" stroke-width=".9"/><path d="M3.2 6h5.6" stroke="#fff" stroke-width=".9"/></svg>
        www.govelmora.com
      </li>
    </ul>

    <div class="band">www.govelmora.com</div>
  </section>
</body>
</html>
```